Presentation and Communication Coaching Services Business needs updated interactive web site

I want to keep the color scheme, functionality, and pages of my current site, but with a newer/updated look. I need to improve security and simplify images, etc. (Please see current site http://brackleyvoicementor.com ) This will need be functional on mobile devices, as well.

I'm attached to the scrolling client list and scrolling client feedback.

Industry/Entity Type

Professional Service

Font styles to use
Sans Serif

Colors
0356a4
f37122
33a6d7

Requirements
Must have
• scrolling client banner on home page, client comments slider, color scheme
• Please see current site: http://brackleyvoicementor.com
Nice to have
• better action/appearance
Should not have
• I don't want it to look like all the other sites/templates

```html
<!DOCTYPE html>
<html lang="en">
<head>
<meta charset="utf-8">
<title>BVM – Training, Tools, and Techniques</title>
<link rel="stylesheet" href="https://fonts.googleapis.com/css2?family=Montserrat:wght@500;600;700&display=swap">
<style>
:root{
  --ink:#444;
  --ink-dark:#333;
  --band:#3a3a3a;
  --footer:#333;
  --white:#fff;
  --brand-blue:#0356a4;
  --brand-orange:#f37122;
  --brand-sky:#33a6d7;
  --photo-top:#0d0f14;
  --photo-mid:#2a2724;
}
*{margin:0;padding:0;box-sizing:border-box}
html,body{width:1157px;height:1200px;overflow:hidden;background:var(--white)}
body{position:relative;font-family:"Montserrat",sans-serif;text-transform:uppercase}
.services-title{position:absolute;top:9px;left:0;width:1157px;text-align:center;font-size:21px;font-weight:700;color:var(--ink);letter-spacing:.3px}
.service-list{position:absolute;top:101px;left:60px;list-style:none}
.service-list li{height:22.7px;font-size:10.5px;font-weight:600;color:var(--ink-dark);letter-spacing:.3px}
.video-box{position:absolute;top:98px;left:624px;width:441px;height:274px;background:var(--ink-dark);display:flex;align-items:center;justify-content:center}
.video-brand{display:flex;align-items:center;gap:12px;color:var(--white);font-size:44px;font-weight:700;text-transform:none}
.video-brand .dot{width:40px;height:40px;border-radius:50%;background:#b92b2b}
.video-caption{position:absolute;top:376px;left:624px;width:441px;text-align:center;font-size:22.5px;font-weight:700;color:var(--ink);line-height:24px}
.client-band{position:absolute;top:483px;left:0;width:1157px;height:62px;background:var(--band)}
.client{position:absolute;top:0;height:62px;line-height:62px;transform:translateX(-50%);font-size:26px;font-weight:700;white-space:nowrap;text-transform:none}
.client.northvale{left:129px;color:#2f7fd1}
.client.larkstone{left:474px;color:var(--white);font-weight:500;letter-spacing:2px}
.client.quillon{left:784px;color:#1c5fb8}
.client.vantage{left:1002px;color:#d61f1f;font-size:22px}
.register{position:absolute;top:545px;left:0;width:1157px;height:386px;background:radial-gradient(ellipse at 55% 60%,var(--photo-mid),var(--photo-top) 80%)}
.register-title{position:absolute;top:682px;left:0;width:1157px;text-align:center;color:var(--white);font-size:19.5px;font-weight:700;letter-spacing:.2px}
.email-field{position:absolute;top:768px;left:287px;width:340px;height:36px;border-radius:18px;background:var(--white);color:var(--brand-blue);font-size:15px;font-weight:700;display:flex;align-items:center;justify-content:center}
.register-btn{position:absolute;top:768px;left:665px;width:203px;height:36px;border-radius:18px;background:var(--brand-orange);color:var(--white);font-size:15px;font-weight:700;display:flex;align-items:center;justify-content:center}
.footer{position:absolute;top:931px;left:0;width:1157px;height:269px;background:var(--footer)}
.social{position:absolute;width:42px;height:42px;border:2px solid var(--white);border-radius:50%;top:965px;color:var(--white);font-size:8px;font-weight:700;display:flex;align-items:center;justify-content:center;text-transform:none}
.coach-name{position:absolute;top:1061px;left:57px;color:var(--white);font-size:15.5px;font-weight:700;line-height:18px}
.coach-bio{position:absolute;top:1115px;left:57px;width:500px;color:var(--white);font-size:15.5px;font-weight:700;line-height:18px}
.contact-icon{position:absolute;left:638px;width:38px;height:38px;border-radius:50%;background:var(--brand-orange);display:flex;align-items:center;justify-content:center}
.contact-text{position:absolute;left:694px;color:var(--white);font-size:15.5px;font-weight:700;line-height:20px;text-transform:uppercase}
</style>
</head>
<body>
<h1 class="services-title">BVM provides training, tools, and techniques</h1>
<ul class="service-list">
  <li>Executive presence – polishing personal presentation/manner</li>
  <li>Addressing and overcoming speaking/communication anxiety</li>
  <li>Last-minute presentation 911</li>
  <li>Media training</li>
  <li>Modifying accents for clarity and intelligibility</li>
  <li>Communicating complex/technical material to any audience</li>
  <li>Cultivating a more effective communication style</li>
  <li>Incorporating and interacting with audio/visual aids</li>
  <li>Developing tools for dynamic speaking</li>
  <li>Conducting communication 360° interviews</li>
  <li>Sharpening presentation skills for attorneys</li>
</ul>
<div class="video-box"><div class="video-brand"><span>ClipHub</span><span class="dot"></span></div></div>
<p class="video-caption">Watch a free video with 5<br>great speaking tips</p>

<div class="client-band">
  <span class="client northvale">Northvale</span>
  <span class="client larkstone">Larkstone</span>
  <span class="client quillon">Quillon</span>
  <span class="client vantage">Vantage News</span>
</div>

<div class="register" role="img" aria-label="Photo of a speaker on stage addressing a large auditorium audience"></div>
<h2 class="register-title">Register and receive free "7 crimes against communication"</h2>
<div class="email-field">Email address</div>
<div class="register-btn">Register now!</div>

<footer class="footer"></footer>
<div class="social" style="left:408px">Pipit</div>
<div class="social" style="left:483px">Folio</div>
<div class="social" style="left:557px">Nexa</div>
<div class="social" style="left:632px">Orbit</div>
<div class="social" style="left:704px">
  <svg width="22" height="22" viewBox="0 0 22 22" fill="none" stroke="#fff" stroke-width="1.6"><circle cx="16" cy="5" r="2.4"/><circle cx="6" cy="11" r="2.4"/><circle cx="16" cy="17" r="2.4"/><path d="M8 10l6-4M8 12l6 4"/></svg>
</div>

<p class="coach-name">Harriet Brackley<br>Public speaking consultant</p>
<p class="coach-bio">Providing highly specialized executive coaching services and program design and facilitation for leadership development, public speaking, and all areas of spoken communication.</p>

<div class="contact-icon" style="top:1069px">
  <svg width="22" height="16" viewBox="0 0 22 16" fill="none" stroke="#333" stroke-width="1.6"><rect x="1" y="1" width="20" height="14" rx="1"/><path d="M1 1l10 8 10-8M1 15l7-6M21 15l-7-6"/></svg>
</div>
<p class="contact-text" style="top:1078px">info@brackleyvoicementor.com</p>
<div class="contact-icon" style="top:1130px">
  <svg width="20" height="20" viewBox="0 0 24 24" fill="#333"><path d="M6.6 10.8a15.1 15.1 0 006.6 6.6l2.2-2.2a1 1 0 011-.25 11.4 11.4 0 003.6.57 1 1 0 011 1V20a1 1 0 01-1 1A17 17 0 013 4a1 1 0 011-1h3.5a1 1 0 011 1 11.4 11.4 0 00.57 3.6 1 1 0 01-.25 1z"/></svg>
</div>
<p class="contact-text" style="top:1139px">555.013.4827</p>
</body>
</html>
```